RV park billboard

We need a billboard for cedar bend RV park . I was thinking about having a big orange in the background. We will have free fiber optic internet and each camper will have its own personal hotspot and we want that on the sign... Also the phone number with the area code... But I don't have the exact number yet. Size of sign will be 12 x 40
Updates
Make sure sign has Cedar Bend RV park on it
Target Market(s)
Plant turnaround workers
Look and feel

```html
<!DOCTYPE html>
<html lang="en">
<head>
<meta charset="utf-8">
<title>Cedar Bend RV park – Billboard</title>
<link rel="stylesheet" href="https://fonts.googleapis.com/css2?family=Oswald:wght@500;600&display=swap">
<style>
  :root {
    --stage: #eef1f4;
    --board-warm: #fbb832;
    --board-hot: #f07a35;
    --citrus-light: #fcbd3a;
    --citrus-deep: #f39a2c;
    --promo-red: #e8262a;
    --title-white: #ffffff;
    --phone-ink: #231f20;
    --device-tone: #3a3a3a;
  }
  html, body {
    margin: 0;
    padding: 0;
    width: 1200px;
    height: 1185px;
    overflow: hidden;
    background: var(--stage);
  }
  .canvas {
    position: relative;
    width: 1200px;
    height: 1185px;
  }
  .billboard {
    position: absolute;
    left: 0;
    top: 412px;
    width: 1200px;
    height: 360px;
    display: block;
  }
  .promo-line {
    font-family: "Oswald", "Arial Narrow", sans-serif;
    font-weight: 600;
    fill: var(--promo-red);
  }
  .park-name {
    font-family: "Oswald", "Arial Narrow", sans-serif;
    font-weight: 600;
    fill: var(--title-white);
  }
  .park-phone {
    font-family: "Oswald", "Arial Narrow", sans-serif;
    font-weight: 600;
    fill: var(--phone-ink);
  }
  .device-area { fill: var(--device-tone); }
</style>
</head>
<body>
<main class="canvas">
  <svg class="billboard" viewBox="0 0 1200 360" xmlns="http://www.w3.org/2000/svg" aria-label="Cedar Bend RV park billboard">
    <defs>
      <linearGradient id="boardGradient" x1="0" y1="0" x2="1" y2="0">
        <stop offset="0" stop-color="var(--board-warm)"/>
        <stop offset="1" stop-color="var(--board-hot)"/>
      </linearGradient>
      <radialGradient id="citrusGradient" cx="0.4" cy="0.35" r="0.7">
        <stop offset="0" stop-color="var(--citrus-light)"/>
        <stop offset="1" stop-color="var(--citrus-deep)"/>
      </radialGradient>
      <clipPath id="boardClip">
        <rect x="0" y="0" width="1200" height="360"/>
      </clipPath>
    </defs>

    <rect class="board-face" x="0" y="0" width="1200" height="360" fill="url(#boardGradient)"/>

    <g clip-path="url(#boardClip)">
      <circle class="big-orange" cx="490" cy="178" r="186" fill="url(#citrusGradient)"
              role="img" aria-label="Illustration of a large orange with a green leaf and stem"/>
    </g>

    <g class="internet-offer">
      <text class="promo-line" x="174" y="99" font-size="50" text-anchor="middle"
            textLength="174" lengthAdjust="spacingAndGlyphs">Free Fiber</text>
      <text class="promo-line" x="175" y="143" font-size="50" text-anchor="middle"
            textLength="245" lengthAdjust="spacingAndGlyphs">Optic Internet</text>

      <rect class="device-area" x="53" y="155" width="233" height="69" rx="4"
            role="img" aria-label="Illustration of a network router with status lights"/>

      <text class="promo-line" x="175" y="286" font-size="50" text-anchor="middle"
            textLength="285" lengthAdjust="spacingAndGlyphs">Personal Hotspot</text>
    </g>

    <text class="park-name" x="815" y="174" font-size="110" text-anchor="middle"
          textLength="705" lengthAdjust="spacingAndGlyphs">Cedar Bend RV park</text>
    <text class="park-phone" x="806" y="308" font-size="124" text-anchor="middle"
          textLength="552" lengthAdjust="spacingAndGlyphs">(913)555-0148</text>
  </svg>
</main>
</body>
</html>
```